Simple menu needed for Asian food truck

We are an Asian food truck that attends big festivals. Our menu is very simple featuring only about 5 or 6 dishes, but we need big pictures and lettering to capture the attention of festival goers. Our motto is "Fresh, Authentic, Homemade", it would be great to include that somewhere. We also need a menu that possibly magnetic so that we can easily take off items that are sold out, change pricing or add different dishes for specific venues. Attached is an example of what our current menu looks like.

```html
<!DOCTYPE html>
<html lang="en">
<head>
<meta charset="utf-8">
<title>Mira's Egg Rolls – Menu</title>
<link rel="stylesheet" href="https://fonts.googleapis.com/css2?family=Oswald:wght@400;500;600&family=Lobster+Two:ital,wght@1,700&display=swap">
<style>
  :root {
    --yellow: #f3d25c;
    --orange: #f7a028;
    --brown: #6a4a3a;
    --white: #ffffff;
    --backdrop: #e9e9e9;
    --card: #ffffff;
    --ink: #333333;
    --card-edge: #8a8a8a;
  }
  * { box-sizing: border-box; margin: 0; padding: 0; }
  html, body { width: 1135px; height: 1200px; overflow: hidden; }
  body { background: var(--backdrop); position: relative; }

  .menu-frame { position: absolute; left: 124px; top: 20px; width: 886px; height: 1160px; }
  .menu {
    position: absolute; left: 0; top: 0; width: 848px; height: 1110px;
    transform: scale(1.0448); transform-origin: 0 0;
    background: var(--white); overflow: hidden;
    box-shadow: 0 8px 24px rgba(0,0,0,.18);
  }
  .band { position: absolute; left: 0; width: 848px; }
  .band--top { top: 0; height: 90px; }
  .band--bottom { bottom: 0; height: 160px; }

  .brand {
    position: absolute; left: 0; width: 848px; top: 70px;
    display: flex; align-items: center; justify-content: center; gap: 10px;
    font-family: 'Oswald', sans-serif; font-weight: 600; font-size: 30px;
    color: var(--orange); letter-spacing: 1px;
  }
  .brand-dot { width: 14px; height: 14px; border-radius: 50%; background: var(--orange); }

  .dish { position: absolute; width: 386px; text-align: center; }
  .dish-photo { position: absolute; border-radius: 14px; }
  .dish-name {
    position: absolute; left: 0; width: 100%;
    font-family: 'Oswald', sans-serif; font-weight: 500; font-size: 34px;
    line-height: 1.05; color: var(--brown);
  }
  .dish-note {
    position: absolute; left: 0; width: 100%;
    font-family: 'Lobster Two', cursive; font-style: italic; font-weight: 700;
    font-size: 22px; color: var(--orange); line-height: 1.1;
  }
  .dish-extra {
    position: absolute; left: 0; width: 100%;
    font-family: 'Oswald', sans-serif; font-weight: 400; font-size: 17px;
    color: var(--ink); line-height: 1.4;
  }
  .price {
    position: absolute; width: 110px; height: 110px; border-radius: 50%;
    background: var(--orange); color: var(--white);
    display: flex; flex-direction: column; align-items: center; justify-content: center;
  }
  .price-label {
    font-family: 'Lobster Two', cursive; font-style: italic; font-weight: 700;
    font-size: 19px; line-height: 1; margin-top: -4px;
  }
  .price-amount {
    font-family: 'Oswald', sans-serif; font-weight: 600; font-size: 58px; line-height: 1;
  }

  .footer-handle {
    position: absolute; left: 56px; top: 1022px; color: var(--white);
    font-family: 'Lobster Two', cursive; font-style: italic; font-weight: 700; font-size: 20px;
    display: flex; align-items: center; gap: 6px;
  }
  .handle-mark { width: 9px; height: 9px; background: var(--white); border-radius: 2px; }
  .footer-motto {
    position: absolute; left: 56px; top: 1050px; color: var(--white);
    font-family: 'Oswald', sans-serif; font-weight: 500; font-size: 29px; letter-spacing: .3px;
  }
  .payments { position: absolute; right: 56px; top: 1020px; text-align: right; }
  .payments-title {
    color: var(--white); font-family: 'Lobster Two', cursive; font-style: italic;
    font-weight: 700; font-size: 19px; margin-bottom: 8px;
  }
  .payment-cards { display: flex; gap: 6px; }
  .payment-card {
    width: 63px; height: 39px; background: var(--card); border-radius: 4px;
    border: 2px solid var(--card-edge);
  }
</style>
</head>
<body>
<div class="menu-frame">
  <main class="menu">
    <svg class="band band--top" viewBox="0 0 848 90" preserveAspectRatio="none" aria-hidden="true">
      <path d="M0 0 H848 V84 Q560 -10 424 14 Q230 -2 0 60 Z" fill="var(--yellow)"/>
    </svg>

    <div class="brand"><span class="brand-dot"></span>MIRA'S EGG ROLLS</div>

    <section class="dish" style="left:34px; top:120px; height:290px;">
      <div class="dish-photo" role="img" aria-label="Three chicken egg rolls in a paper tray with a cup of sweet chili sauce"
           style="left:30px; top:0; width:300px; height:205px; background:radial-gradient(ellipse at 55% 55%, #e2b56a 0%, #f1dcaa 45%, #fbf6ec 75%);"></div>
      <div class="price" style="left:246px; top:108px;"><span class="price-label">3 for</span><span class="price-amount">$6</span></div>
      <h2 class="dish-name" style="top:218px;">Chicken Eggrolls</h2>
    </section>

    <section class="dish" style="left:420px; top:120px; height:290px;">
      <div class="dish-photo" role="img" aria-label="Two fresh shrimp spring rolls in a paper tray with dipping sauces"
           style="left:10px; top:10px; width:340px; height:200px; background:radial-gradient(ellipse at 55% 55%, #f3d0c0 0%, #eef1ea 50%, #fbfbfa 78%);"></div>
      <div class="price" style="left:251px; top:108px;"><span class="price-label">2 for</span><span class="price-amount">$6</span></div>
      <h2 class="dish-name" style="top:218px;">Fresh Springrolls</h2>
      <p class="dish-note" style="top:262px;">Shrimp or Veggie</p>
    </section>

    <section class="dish" style="left:34px; top:402px; height:300px;">
      <div class="dish-photo" role="img" aria-label="Two Chinese BBQ pork skewers in a paper tray"
           style="left:40px; top:0; width:300px; height:200px; background:radial-gradient(ellipse at 50% 55%, #8a1d2c 0%, #c9707a 40%, #f6eeee 75%);"></div>
      <div class="price" style="left:246px; top:106px;"><span class="price-label">2 for</span><span class="price-amount">$6</span></div>
      <h2 class="dish-name" style="top:216px;">Chinese BBQ Pork<br>Skewers</h2>
    </section>

    <section class="dish" style="left:420px; top:402px; height:300px;">
      <div class="dish-photo" role="img" aria-label="Bowl of fried rice with vegetables and pork in a paper tray"
           style="left:10px; top:20px; width:340px; height:185px; background:radial-gradient(ellipse at 50% 45%, #d9b574 0%, #eedcb4 45%, #fbf8f1 78%);"></div>
      <div class="price" style="left:251px; top:106px;"><span class="price-label">Bowl</span><span class="price-amount">$5</span></div>
      <h2 class="dish-name" style="top:216px;">Fried Rice</h2>
      <p class="dish-note" style="top:258px;">Chicken or Pork</p>
    </section>

    <section class="dish" style="left:34px; top:690px; height:300px;">
      <div class="dish-photo" role="img" aria-label="Stuffed chicken wing with a side of fried rice in a takeout box"
           style="left:20px; top:10px; width:360px; height:185px; background:radial-gradient(ellipse at 55% 45%, #e8c46e 0%, #f1e1b8 45%, #fbf9f3 78%);"></div>
      <div class="price" style="left:246px; top:88px;"><span class="price-label">Combo</span><span class="price-amount">$8</span></div>
      <h2 class="dish-name" style="top:196px;">Angel Wing</h2>
      <p class="dish-note" style="top:234px;">Stuffed Chicken Wing</p>
      <p class="dish-extra" style="top:260px;">WITH SIDE OF FRIED RICE</p>
    </section>

    <section class="dish" style="left:420px; top:690px; height:300px;">
      <div class="dish-photo" role="img" aria-label="Three glasses of strawberry, mango and peach flavored tea"
           style="left:100px; top:20px; width:200px; height:175px; background:linear-gradient(90deg, #ec3e5a 0%, #f8c23a 50%, #f5a55a 100%); opacity:.85;"></div>
      <div class="price" style="left:251px; top:88px;"><span class="price-amount">$5</span></div>
      <h2 class="dish-name" style="top:196px;">Flavored Tea</h2>
      <p class="dish-note" style="top:234px;">Strawberry, Mango<br>or Peach</p>
    </section>

    <svg class="band band--bottom" viewBox="0 0 848 160" preserveAspectRatio="none" aria-hidden="true">
      <path d="M0 16 Q424 110 848 2 V160 H0 Z" fill="var(--orange)"/>
    </svg>

    <p class="footer-handle"><span class="handle-mark"></span>/MirasAuthenticEggRolls</p>
    <p class="footer-motto">FRESH • AUTHENTIC • HOMEMADE</p>
    <div class="payments">
      <p class="payments-title">We accept card payments</p>
      <div class="payment-cards">
        <span class="payment-card"></span>
        <span class="payment-card"></span>
        <span class="payment-card"></span>
        <span class="payment-card"></span>
      </div>
    </div>
  </main>
</div>
</body>
</html>
```